County Surplus Auction

This postcard is advertising the upcoming Brindle County Surplus Equipment Auction we are conducting. The auction will be online only and will open on Monday, June 1 at 11:00 a.m. and close on Tuesday, June 2 at 2:00 p.m. Advertise our website www.tkvbids.example and our phone number 770-555-0147 very visibly, and this license number has to be included, but does not need to be very large GA Firm Lic #C7316. Please also advertise pre-auction viewing dates of Thursday, May 28 and Friday May 29, 11:00 a.m. until 3:00 p.m. both days.

```html
<!DOCTYPE html>
<html lang="en">
<head>
<meta charset="utf-8">
<title>Brindle County Surplus Equipment Online Auction – Postcards</title>
<link href="https://fonts.googleapis.com/css2?family=Source+Sans+3:ital,wght@0,400;0,600;0,700;1,400;1,600;1,700&display=swap" rel="stylesheet">
<style>
  :root {
    --gold: #a98225;
    --gold-light: #c9a75a;
    --gold-pale: #ead9b0;
    --cream: #f6efdf;
    --brown: #3a2610;
    --copper: #8a5a1c;
    --white: #ffffff;
    --stage: #ece7de;
    --photo-tractor: #7f6a55;
    --photo-sedan: #8a3a3f;
    --photo-crane: #6f7a5a;
    --photo-laptop: #cfd6de;
  }
  * { margin: 0; padding: 0; box-sizing: border-box; }
  html, body { width: 1131px; height: 1200px; overflow: hidden; }
  body {
    background: var(--stage);
    font-family: "Source Sans 3", "Myriad Pro", Arial, sans-serif;
    color: var(--brown);
    position: relative;
  }
  .postcard {
    position: absolute;
    background: var(--white);
    overflow: hidden;
    box-shadow: 0 3px 10px rgba(0,0,0,.25);
  }
  .postcard--wide { left: 74px; top: 46px; width: 813px; height: 529px; }
  .postcard--side { left: 235px; top: 624px; width: 812px; height: 526px; }

  .photo { position: absolute; }
  .photo--tractor { background: linear-gradient(180deg, #a9c4e0 0%, #9a7d63 45%, var(--photo-tractor) 100%); }
  .photo--sedan { background: linear-gradient(180deg, #b3cde6 0%, #b7b4ad 35%, var(--photo-sedan) 70%, #7d7a74 100%); }
  .photo--crane { background: linear-gradient(180deg, #4f88c9 0%, #8f9a78 45%, var(--photo-crane) 75%, #3d3d3d 100%); }
  .photo--laptop { background: radial-gradient(ellipse at 55% 50%, #e6ebf0 0%, var(--photo-laptop) 55%, #ffffff 90%); }

  .header-band {
    position: absolute;
    background: linear-gradient(180deg, var(--gold-light) 0%, var(--gold) 100%);
    text-align: center;
  }
  .event-title {
    font-style: italic;
    font-weight: 600;
    color: var(--white);
    font-size: 36px;
    line-height: 1;
    letter-spacing: .2px;
  }
  .event-type {
    font-weight: 700;
    color: var(--brown);
    font-size: 34px;
    letter-spacing: 3px;
    line-height: 1;
  }

  .dates { font-weight: 600; color: var(--brown); }
  .viewing { font-style: italic; color: var(--copper); }
  .contact {
    font-style: italic; font-weight: 700; color: var(--brown);
    display: flex; align-items: center; gap: 8px; white-space: nowrap;
  }
  .phone-icon { flex: none; }
  .license { font-size: 12px; color: var(--brown); text-align: right; }

  .wave-footer { position: absolute; left: 0; bottom: 0; width: 100%; }

  /* wide card */
  .postcard--wide .photo--laptop { left: 0; top: 0; width: 174px; height: 116px; }
  .postcard--wide .header-band { left: 174px; top: 0; width: 639px; height: 116px; padding-top: 22px; }
  .postcard--wide .event-type { margin-top: 10px; }
  .postcard--wide .gold-strip { position: absolute; left: 0; top: 116px; width: 100%; height: 14px; background: linear-gradient(180deg, var(--gold-pale), var(--cream)); }
  .postcard--wide .photo--tractor { left: 2px; top: 131px; width: 254px; height: 179px; }
  .postcard--wide .photo--sedan { left: 266px; top: 131px; width: 267px; height: 179px; }
  .postcard--wide .photo--crane { left: 542px; top: 131px; width: 270px; height: 179px; }
  .postcard--wide .dates {
    position: absolute; left: 0; top: 326px; width: 100%; text-align: center;
    font-size: 27px; line-height: 34px; text-decoration: underline; text-underline-offset: 4px;
  }
  .postcard--wide .viewing {
    position: absolute; left: 0; top: 396px; width: 100%; text-align: center;
    font-size: 18px; line-height: 22px;
  }
  .postcard--wide .contact--phone { position: absolute; left: 17px; top: 462px; font-size: 32px; }
  .postcard--wide .contact--web { position: absolute; right: 22px; top: 462px; font-size: 29px; }
  .postcard--wide .license { position: absolute; right: 26px; top: 497px; }

  /* side card */
  .postcard--side .header-band { left: 0; top: 0; width: 600px; height: 114px; padding-top: 26px; }
  .postcard--side .event-title { font-size: 34.5px; }
  .postcard--side .event-type { margin-top: 13px; }
  .postcard--side .photo-column {
    position: absolute; left: 585px; top: 0; width: 227px; height: 460px;
    background: linear-gradient(90deg, var(--white) 0%, var(--gold-pale) 40%, var(--gold-light) 100%);
  }
  .postcard--side .photo--tractor { left: 603px; top: 18px; width: 180px; height: 128px; }
  .postcard--side .photo--sedan { left: 603px; top: 161px; width: 180px; height: 127px; }
  .postcard--side .photo--crane { left: 603px; top: 304px; width: 180px; height: 127px; }
  .postcard--side .dates {
    position: absolute; left: 17px; top: 137px; width: 570px;
    font-size: 29.5px; line-height: 34px;
  }
  .postcard--side .viewing {
    position: absolute; left: 17px; top: 255px; font-size: 21px; line-height: 26px;
  }
  .postcard--side .contact--web { position: absolute; left: 22px; top: 345px; font-size: 30px; }
  .postcard--side .contact--phone { position: absolute; left: 22px; top: 392px; font-size: 32px; }
  .postcard--side .photo--laptop { left: 362px; top: 300px; width: 210px; height: 122px; }
</style>
</head>
<body>

<article class="postcard postcard--wide">
  <div class="photo photo--laptop" role="img" aria-label="Hand holding a gavel reaching out of a laptop screen"></div>
  <header class="header-band">
    <h1 class="event-title">Brindle County Surplus Equipment</h1>
    <p class="event-type">ONLINE AUCTION</p>
  </header>
  <div class="gold-strip"></div>
  <div class="photo photo--tractor" role="img" aria-label="Red farm tractor parked on grass"></div>
  <div class="photo photo--sedan" role="img" aria-label="Red sedan in a parking lot"></div>
  <div class="photo photo--crane" role="img" aria-label="Camouflage-painted mobile crane"></div>
  <p class="dates">The auction will be online only and will open on Monday,<br>June 1 at 11:00 a.m. and close on Tuesday, June 2 at 2:00 p.m</p>
  <p class="viewing">Pre-auction viewing dates: Thursday, May 28 and Friday, May 29,<br>11:00 a.m. until 3:00 p.m. both days.</p>
  <svg class="wave-footer" width="813" height="90" viewBox="0 0 813 90" preserveAspectRatio="none" aria-hidden="true">
    <path d="M0 8 C200 -6 420 30 813 6 L813 90 L0 90 Z" fill="#e9d9b2"/>
    <path d="M0 22 C230 8 450 44 813 20 L813 90 L0 90 Z" fill="#d8bf83"/>
    <path d="M0 48 C260 34 480 70 813 46 L813 90 L0 90 Z" fill="#b99440"/>
    <path d="M0 74 C260 62 500 88 813 70 L813 90 L0 90 Z" fill="#a98225"/>
  </svg>
  <p class="contact contact--phone">
    <svg class="phone-icon" width="40" height="40" viewBox="0 0 40 40" aria-hidden="true"><circle cx="20" cy="20" r="17.5" fill="none" stroke="#3a2610" stroke-width="3"/><path d="M14 10 l4 0 l2 6 l-3 2 c1.5 3 3.5 5 6 6 l2 -3 l6 2 l0 4 c-10 1 -18 -7 -17 -17 z" fill="#3a2610"/></svg>
    <span>770-555-0147</span>
  </p>
  <p class="contact contact--web">www.tkvbids.example</p>
  <p class="license">GA Firm Lic #C7316</p>
</article>

<article class="postcard postcard--side">
  <div class="photo-column"></div>
  <header class="header-band">
    <h1 class="event-title">Brindle County Surplus Equipment</h1>
    <p class="event-type">ONLINE AUCTION</p>
  </header>
  <div class="photo photo--tractor" role="img" aria-label="Red farm tractor parked on grass"></div>
  <div class="photo photo--sedan" role="img" aria-label="Red sedan in a parking lot"></div>
  <div class="photo photo--crane" role="img" aria-label="Camouflage-painted mobile crane"></div>
  <p class="dates">The auction will be online only and will<br>open on Monday, June 1 at 11:00 a.m.<br>and close on Tuesday, June 2 at 2:00 p.m</p>
  <p class="viewing">Pre-auction viewing dates:<br>Thursday, May 28 and Friday, May 29,<br>11:00 a.m. until 3:00 p.m. both days.</p>
  <div class="photo photo--laptop" role="img" aria-label="Hand holding a gavel reaching out of a laptop screen"></div>
  <p class="contact contact--web">www.tkvbids.example</p>
  <p class="contact contact--phone">
    <svg class="phone-icon" width="44" height="44" viewBox="0 0 40 40" aria-hidden="true"><circle cx="20" cy="20" r="17.5" fill="none" stroke="#3a2610" stroke-width="3"/><path d="M14 10 l4 0 l2 6 l-3 2 c1.5 3 3.5 5 6 6 l2 -3 l6 2 l0 4 c-10 1 -18 -7 -17 -17 z" fill="#3a2610"/></svg>
    <span>770-555-0147</span>
  </p>
  <svg class="wave-footer" width="812" height="92" viewBox="0 0 812 92" preserveAspectRatio="none" aria-hidden="true">
    <path d="M0 10 C220 -4 430 30 812 8 L812 92 L0 92 Z" fill="#e9d9b2"/>
    <path d="M0 26 C240 12 460 46 812 24 L812 92 L0 92 Z" fill="#d8bf83"/>
    <path d="M0 50 C260 36 490 72 812 48 L812 92 L0 92 Z" fill="#b99440"/>
    <path d="M0 76 C260 64 500 90 812 72 L812 92 L0 92 Z" fill="#a98225"/>
  </svg>
</article>

</body>
</html>
```